Casa Vero Inspections Business Card

I need a business card for my new company. The company is going to provide home inspections. The name of the company is Casa Vero Inspections. I am not sure if I want a single sided card or a double. I have a logo already that I want to incorporate into the card design. I was wondering if I should incorporate a catch phrase on my card or not. If I did the phrase would be "The Intelligent Choice for Home Inspections" but i am unsure how or if to use it on a card. The following information needs to be on the card.
Home Inspection
My Name: Marcus T. Wolford Phone Number: 555-301-7762 Email: mwolford@casaveroinspections.com Website: www.casaveroinspections.com NY HI License # 27300519462

```html
<!DOCTYPE html>
<html lang="en">
<head>
<meta charset="utf-8">
<title>Casa Vero Inspections — Business Card</title>
<link rel="stylesheet" href="https://fonts.googleapis.com/css2?family=Montserrat:wght@400;500;700&family=Fira+Sans:wght@600&display=swap">
<style>
  :root {
    --brand-blue: #0a68a8;
    --brand-blue-back: #0d6fad;
    --sky-blue: #78c3ec;
    --ink: #1c1c1c;
    --card-white: #ffffff;
    --page-bg: #e9eaec;
  }
  * { margin: 0; padding: 0; box-sizing: border-box; }
  html, body {
    width: 1093px;
    height: 1200px;
    overflow: hidden;
    background: var(--page-bg);
    font-family: "Montserrat", sans-serif;
  }
  .canvas {
    position: relative;
    width: 1093px;
    height: 1200px;
  }
  .card {
    position: absolute;
    border-radius: 20px;
    overflow: hidden;
  }

  /* Front */
  .card--front {
    left: 265px;
    top: 225px;
    width: 580px;
    height: 363px;
    background: var(--card-white);
  }
  .wordmark {
    position: absolute;
    left: 0;
    width: 100%;
    text-align: center;
    font-weight: 700;
    font-size: 33px;
    letter-spacing: 0.5px;
  }
  .card--front .wordmark {
    top: 98px;
    color: var(--brand-blue);
  }
  .holder-name {
    position: absolute;
    right: 322px;
    top: 242px;
    text-align: right;
    font-weight: 700;
    font-size: 21px;
    color: var(--brand-blue);
    white-space: nowrap;
  }
  .divider {
    position: absolute;
    left: 269px;
    top: 223px;
    width: 1.5px;
    height: 64px;
    background: var(--brand-blue);
  }
  .contact-list {
    position: absolute;
    left: 281px;
    top: 220px;
    list-style: none;
  }
  .contact-item {
    display: flex;
    align-items: center;
    height: 24.5px;
    font-size: 13px;
    font-weight: 500;
    color: var(--ink);
    white-space: nowrap;
  }
  .contact-icon {
    width: 16px;
    height: 16px;
    margin-right: 11px;
    flex: none;
  }
  .license {
    position: absolute;
    left: 0;
    top: 302px;
    width: 100%;
    text-align: center;
    font-size: 12.5px;
    font-weight: 500;
    color: var(--ink);
  }
  .wave {
    position: absolute;
    left: 0;
    top: 0;
    width: 580px;
    height: 363px;
  }

  /* Back */
  .card--back {
    left: 259px;
    top: 616px;
    width: 595px;
    height: 366px;
    background: var(--brand-blue-back);
  }
  .card--back .wordmark {
    top: 150px;
    font-size: 34px;
    color: var(--card-white);
  }
  .tagline {
    position: absolute;
    left: 0;
    top: 316px;
    width: 100%;
    text-align: center;
    font-family: "Fira Sans", sans-serif;
    font-weight: 600;
    font-size: 13.5px;
    color: var(--card-white);
  }
</style>
</head>
<body>
<main class="canvas">

  <section class="card card--front" aria-label="Card front">
    <svg class="wave" viewBox="0 0 580 363" aria-hidden="true">
      <path d="M0,305 Q290,369 580,305 L580,363 L0,363 Z" fill="var(--brand-blue)"/>
      <path d="M65,309 Q290,350 515,309" fill="none" stroke="var(--sky-blue)" stroke-width="2.5"/>
    </svg>

    <div class="wordmark">Casa Vero Inspections</div>

    <div class="holder-name">Marcus T. Wolford</div>
    <div class="divider"></div>

    <ul class="contact-list">
      <li class="contact-item">
        <svg class="contact-icon" viewBox="0 0 16 16" aria-hidden="true">
          <path d="M3.5 1.5l2.4 2.6-1.3 1.8c.8 1.9 2.4 3.5 4.4 4.5l1.8-1.3 2.6 2.3-1.6 2.6C6.8 13.6 2.4 9.2 1 3.1z" fill="var(--brand-blue)"/>
          <path d="M9.5 2.5a4.5 4.5 0 0 1 4 4M9.5 5a2 2 0 0 1 1.6 1.6" fill="none" stroke="var(--brand-blue)" stroke-width="1.2" stroke-linecap="round"/>
        </svg>
        555-301-7762
      </li>
      <li class="contact-item">
        <svg class="contact-icon" viewBox="0 0 16 16" aria-hidden="true">
          <rect x="1.5" y="4" width="12" height="8" rx="0.8" fill="var(--brand-blue)"/>
          <path d="M1.8 4.5l5.7 4 5.7-4" fill="none" stroke="#fff" stroke-width="1"/>
        </svg>
        mwolford@casaveroinspections.com
      </li>
      <li class="contact-item">
        <svg class="contact-icon" viewBox="0 0 16 16" aria-hidden="true">
          <circle cx="7.5" cy="8" r="6" fill="var(--brand-blue)"/>
          <path d="M4 5.5c1.5-.5 2.5.5 2 1.8-.5 1.2 1 1.8 1 3.2M9.5 3.5c.5 1.2 2 1.2 2.5 2.5M9 11c.8-.8 2-.6 2.6.2" fill="none" stroke="#fff" stroke-width="1"/>
        </svg>
        www.casaveroinspections.com
      </li>
    </ul>

    <div class="license">NY HI License # 27300519462</div>
  </section>

  <section class="card card--back" aria-label="Card back">
    <div class="wordmark">Casa Vero Inspections</div>
    <p class="tagline">The Intelligent Choice for Home Inspections</p>
  </section>

</main>
</body>
</html>
```